Trifold for International Business Consulting firm

I have created a trifold piece (attached) that includes all the necessary information in a Word template; however, I need a professional that can make it look "current, international and modern". Our website, brenvaleadvisory.com, should give an idea as to the style and color template we like.

```html
<!DOCTYPE html>
<html lang="en">
<head>
<meta charset="utf-8">
<title>Brenvale Advisory – Trifold</title>
<link href="https://fonts.googleapis.com/css2?family=Open+Sans:wght@300;400;600;700&family=Tinos&display=swap" rel="stylesheet">
<style>
  :root {
    --stage: #4a4a4c;
    --paper: #f4f4f6;
    --ink: #2b2b2e;
    --ink-soft: #4a4a50;
    --green-band: #c9d684;
    --green-label: #a9c03a;
    --rule: #cdd59a;
    --fold: #dcdce2;
    --peak-light: #d9dde3;
    --peak-mid: #9aa6b5;
    --peak-dark: #5e6b7d;
  }
  * { box-sizing: border-box; margin: 0; padding: 0; }
  html, body { width: 1200px; height: 838px; overflow: hidden; }
  body {
    background: var(--stage);
    font-family: "Open Sans", Arial, sans-serif;
    color: var(--ink);
  }
  .trifold {
    position: absolute;
    left: 96px; top: 29px;
    width: 1008px; height: 780px;
    background: var(--paper);
    display: grid;
    grid-template-columns: repeat(3, 1fr);
    overflow: hidden;
  }
  .mountain-scene {
    position: absolute;
    left: 0; right: 0; bottom: 0;
    height: 46%;
    background:
      linear-gradient(to bottom, rgba(244,244,246,1) 0%, rgba(244,244,246,0) 38%),
      linear-gradient(160deg, var(--peak-light) 10%, var(--peak-mid) 45%, var(--peak-dark) 60%, var(--peak-mid) 72%, var(--peak-light) 95%);
    z-index: 0;
  }
  .panel {
    position: relative;
    z-index: 1;
    padding: 44px 34px 30px;
    border-right: 1px solid var(--fold);
  }
  .panel:last-child { border-right: none; }

  /* Brand lockup */
  .brand { text-align: center; margin-bottom: 26px; }
  .brand-name {
    font-size: 30px; font-weight: 700; letter-spacing: -0.5px;
    color: var(--ink); line-height: 1;
  }
  .brand-sub {
    font-size: 13px; font-weight: 400; letter-spacing: 7px;
    color: var(--ink); margin-top: 6px; text-transform: uppercase;
  }
  .brand-line { font-size: 6.5px; margin-top: 4px; color: var(--ink-soft); }

  /* Process panel */
  .eyebrow { font-size: 9px; color: var(--ink-soft); margin-bottom: 8px; }
  .band-heading {
    background: var(--green-band);
    font-size: 18px; font-weight: 400;
    padding: 8px 12px; margin-bottom: 16px;
    text-transform: uppercase;
  }
  .process-text { font-size: 14px; line-height: 1.3; margin-bottom: 10px; }
  .steps { list-style: none; margin-bottom: 14px; }
  .steps li {
    display: grid; grid-template-columns: 30px 1fr;
    font-size: 14px; line-height: 1.3; margin-bottom: 6px;
  }
  .step-num {
    width: 20px; height: 20px; border-radius: 50%;
    background: var(--green-band); font-size: 11px;
    display: flex; align-items: center; justify-content: center;
    margin-top: 1px;
  }
  .highlight-box {
    background: var(--green-band);
    font-size: 14px; line-height: 1.3;
    padding: 10px 12px; margin-bottom: 14px;
  }
  .copyright { font-family: "Tinos", "Times New Roman", serif; font-size: 14px; margin-top: 16px; }

  /* Contact panel */
  .contact { padding-top: 150px; }
  .contact-title { font-size: 26px; font-weight: 300; margin-bottom: 36px; text-align: center; }
  .contact-item { margin-bottom: 22px; font-size: 14px; line-height: 1.3; }
  .contact-label { display: block; color: var(--green-label); font-weight: 700; font-size: 13px; }
  .contact-web { font-weight: 700; }

  /* Cover panel */
  .cover { padding-top: 150px; }
  .intro {
    border-top: 1px solid var(--rule); border-bottom: 1px solid var(--rule);
    font-size: 11px; text-transform: uppercase; line-height: 1.35;
    padding: 10px 0; margin-bottom: 26px;
  }
  .mission {
    background: var(--green-band);
    font-size: 15px; text-transform: uppercase; line-height: 1.35;
    padding: 18px 20px; margin-bottom: 26px;
  }
  .benefits {
    list-style: none; font-size: 10.5px; text-transform: uppercase; line-height: 1.6;
    border-top: 1px solid var(--rule); padding-top: 10px; width: 78%; margin-left: auto;
  }
</style>
</head>
<body>
  <main class="trifold">
    <div class="mountain-scene" role="img" aria-label="Snow-covered mountain range fading into the page"></div>

    <section class="panel process">
      <p class="eyebrow">Comprehensive Services • Business Development</p>
      <h2 class="band-heading">Our Three Step Process</h2>
      <p class="process-text">Once you have made the decision to grow your business internationally we follow a very simple and cost efficient path. After our initial contact and agreement:</p>
      <ol class="steps">
        <li><span class="step-num">1.</span><span>Gather necessary information.</span></li>
        <li><span class="step-num">2.</span><span>Perform an onsite company readiness check and presentation.</span></li>
        <li><span class="step-num">3.</span><span>Develop and provide an international strategic path forward.</span></li>
      </ol>
      <p class="highlight-box">Let us manage the entire process for you from strategy to successful execution.</p>
      <p class="process-text">We will assemble and coordinate the needed team of specialists for the project and provide the necessary business contacts for your international growth.</p>
      <p class="copyright">©Northgate Partners Group, LLC.</p>
    </section>

    <section class="panel contact">
      <div class="brand">
        <div class="brand-name">BRENVALE</div>
        <div class="brand-sub">Advisory</div>
        <div class="brand-line">International Business and Public Affairs Development</div>
      </div>
      <h2 class="contact-title">CONTACT US</h2>
      <p class="contact-item"><span class="contact-label">ADDRESS</span>455 Harlow Ave. Suite 310<br>Denton, TX 76201</p>
      <p class="contact-item"><span class="contact-label">PHONE</span>(555) 014-2276</p>
      <p class="contact-item"><span class="contact-label">WEB</span><span class="contact-web">brenvaleadvisory.com</span></p>
    </section>

    <section class="panel cover" style="padding-top:44px">
      <div class="brand">
        <div class="brand-name">BRENVALE</div>
        <div class="brand-sub">Advisory</div>
        <div class="brand-line">International Business and Public Affairs Development</div>
      </div>
      <p class="intro">Your international business<br>development process<br>begins with us</p>
      <p class="mission">Our effective, innovative growth approach helps midsize organizations accelerate and compete in a global world</p>
      <ul class="benefits">
        <li>Successful low cost</li>
        <li>Low complexity</li>
        <li>World class</li>
        <li>Cloud based business approach</li>
      </ul>
    </section>
  </main>
</body>
</html>
```